Business Card Design Project

we need a business card design for our company: www.plomvik.ch
It's important to include our already existing logo (see website)

```html
<!DOCTYPE html>
<html lang="de">
<head>
<meta charset="utf-8">
<title>Plomvik – Visitenkarten</title>
<link rel="stylesheet" href="https://fonts.googleapis.com/css2?family=PT+Sans:wght@400;700&family=Tinos:wght@400;700&display=swap">
<style>
  :root {
    --page: #ffffff;
    --card: #ffffff;
    --brand-blue: #0b3ea6;
    --brand-light: #5a8fc0;
    --logo-blue: #1d4fa8;
    --ink: #111111;
    --on-brand: #ffffff;
    --rule-grey: #d6d6d6;
    --shadow: rgba(0, 0, 0, 0.28);
  }
  * { margin: 0; padding: 0; box-sizing: border-box; }
  html, body {
    width: 1108px; height: 1200px; overflow: hidden;
    background: var(--page);
  }
  .sheet { position: relative; width: 1108px; height: 1200px; }

  .card {
    position: absolute;
    background: var(--card);
    box-shadow: 4px 6px 10px var(--shadow);
    overflow: hidden;
  }
  .card--front { left: 65px; top: 52px; width: 893px; height: 513px; }
  .card--back  { left: 153px; top: 620px; width: 899px; height: 510px; }

  .holder-name {
    position: absolute;
    font-family: "PT Sans", sans-serif;
    font-weight: 700;
    font-size: 27px;
    color: var(--ink);
    letter-spacing: 0.5px;
    white-space: nowrap;
  }
  .card--front .holder-name { left: 0; width: 100%; text-align: center; top: 27px; }
  .card--back .holder-name { left: 92px; top: 326px; }

  .wordmark {
    position: absolute;
    display: flex; align-items: center; gap: 14px;
    font-family: "PT Sans", sans-serif;
    font-weight: 400;
    color: var(--logo-blue);
    white-space: nowrap;
    line-height: 1;
  }
  .wordmark__square { display: block; background: var(--logo-blue); }
  .card--front .wordmark { left: 0; width: 100%; justify-content: center; top: 175px; font-size: 82px; }
  .card--front .wordmark__square { width: 56px; height: 56px; }
  .card--back .wordmark { left: 22px; top: 22px; font-size: 72px; }
  .card--back .wordmark__square { width: 50px; height: 50px; }

  .brand-band { position: absolute; left: 0; top: 367px; width: 100%; height: 146px; }

  .contact {
    position: absolute;
    font-family: "Tinos", serif;
    white-space: nowrap;
    line-height: 1;
  }
  .contact b { font-weight: 700; }
  .band-text { color: var(--on-brand); font-size: 18px; }
  .contact-line { color: var(--ink); font-size: 19px; }
  .address-line { color: var(--ink); font-size: 20px; }

  .band-address {
    position: absolute; left: 22px; top: 381px; width: 320px;
    font-family: "Tinos", serif; font-size: 18px; line-height: 27px;
    color: var(--on-brand); white-space: nowrap;
  }
  .band-address__city { text-align: right; }
</style>
</head>
<body>
<main class="sheet">

  <section class="card card--front" aria-label="Visitenkarte Vorderseite">
    <div class="holder-name">Eeee Dddd</div>
    <div class="wordmark"><span class="wordmark__square"></span>Plomvik</div>

    <svg class="brand-band" viewBox="0 0 893 146" preserveAspectRatio="none" aria-hidden="true">
      <rect x="0" y="0" width="893" height="146" fill="var(--brand-blue)"/>
      <rect x="0" y="70" width="893" height="13" fill="var(--brand-light)"/>
      <rect x="0" y="97" width="893" height="13" fill="var(--brand-light)"/>
      <rect x="0" y="123" width="893" height="12" fill="var(--brand-light)"/>
    </svg>

    <div class="band-address">
      <div>Plomvik AG&nbsp;&nbsp;Lindenweg 12</div>
      <div class="band-address__city">8004 Zürich</div>
    </div>
    <div class="contact band-text" style="left:393px; top:385px;"><b>Webseite:</b> www.plomvik.ch</div>
    <div class="contact band-text" style="left:638px; top:385px;"><b>Telefon:</b> +41 44 321 67 89</div>
    <div class="contact band-text" style="left:393px; top:412px;"><b>Mail:</b> info@plomvik.ch</div>
    <div class="contact band-text" style="left:638px; top:412px;"><b>Skype:</b> plomvik.ch</div>
  </section>

  <section class="card card--back" aria-label="Visitenkarte Rückseite">
    <div class="wordmark"><span class="wordmark__square"></span>Plomvik</div>

    <svg style="position:absolute; left:0; top:0;" width="899" height="510" viewBox="0 0 899 510" aria-hidden="true">
      <g fill="var(--rule-grey)">
        <rect x="22" y="211" width="59" height="12"/>
        <rect x="22" y="237" width="59" height="12"/>
        <rect x="22" y="263" width="59" height="12"/>
        <rect x="22" y="289" width="59" height="12"/>
        <rect x="22" y="315" width="59" height="12"/>

        <rect x="22" y="357" width="429" height="12"/>
        <rect x="22" y="383" width="429" height="12"/>
        <rect x="22" y="409" width="429" height="12"/>
        <rect x="22" y="435" width="429" height="12"/>
        <rect x="22" y="461" width="429" height="12"/>

        <rect x="814" y="226" width="59" height="12"/>
        <rect x="814" y="252" width="59" height="12"/>
        <rect x="814" y="278" width="59" height="12"/>
        <rect x="814" y="304" width="59" height="12"/>
        <rect x="814" y="330" width="59" height="12"/>
        <rect x="814" y="355" width="59" height="12"/>
        <rect x="814" y="381" width="59" height="12"/>
        <rect x="814" y="407" width="59" height="12"/>
        <rect x="814" y="433" width="59" height="12"/>
        <rect x="814" y="459" width="59" height="12"/>

        <rect x="22" y="479" width="851" height="12"/>
      </g>
    </svg>

    <div class="holder-name">Eeee Dddd</div>

    <div class="contact address-line" style="left:471px; top:210px;">Plomvik AG</div>
    <div class="contact address-line" style="left:471px; top:238px;">Lindenweg 12</div>
    <div class="contact address-line" style="left:471px; top:266px;">8004 Zürich</div>

    <div class="contact contact-line" style="left:471px; top:364px;"><b>Webseite:</b> www.plomvik.ch</div>
    <div class="contact contact-line" style="left:471px; top:391px;"><b>Telefon:</b> +41 44 321 67 89</div>
    <div class="contact contact-line" style="left:471px; top:418px;"><b>Mail:</b> info@plomvik.ch</div>
    <div class="contact contact-line" style="left:471px; top:446px;"><b>Skype:</b> plomvik.ch</div>
  </section>

</main>
</body>
</html>
```